Business card design incorporating discount offer

We are a trade services company and we need a double sided business card that is going to be used by our tradesmen to give to customers on completion of their jobs.

Below are the key elements of the card that we would like to include:

-Main logo with text 'Expert Property Care' underneath.
-Up to 12 smaller icon logos with text 'Your local all-trade experts' to emphasise the point that we cover all the trades
-Discount offer - 10% discount
-Telephone number and website address
-Blank space for tradesman to enter his/her name
-Request for customer feedback with feedback url

This business card will be printed on regular card. In the past we have favoured designs that use a black background but we're open to new ideas.

I have attached a few files:

-A simple wire frame example to show how this card could look with the different elements mentioned above, feel free to use a layout similar to this or come up with something totally different (biz-card.pdf)
-Front and back of a loyalty card the we've used in the past (this card was printed on plastic)
-Front and back of a key fob design that we've previously used (this card was printed on plastic)
-A logo file with the 12 small icons and the main logo image

If you need further images or information please ask.

```html
<!DOCTYPE html>
<html lang="en">
<head>
<meta charset="utf-8">
<title>Norvale Business Card – Front and Back</title>
<link href="https://fonts.googleapis.com/css2?family=Varela+Round&display=swap" rel="stylesheet">
<style>
  :root {
    --bg: #e9e6e1;
    --card: #fbfbfb;
    --blue: #1e9fd6;
    --blue-dark: #0f7fc0;
    --blue-light: #4fc3ec;
    --grey: #8c8c8c;
    --grey-light: #a9a9a9;
    --rule: #cfd6da;
  }
  * { margin: 0; padding: 0; box-sizing: border-box; }
  html, body { width: 1200px; height: 1000px; overflow: hidden; }
  body {
    background: var(--bg);
    font-family: "Varela Round", "Helvetica Neue", Arial, sans-serif;
    position: relative;
  }
  .card {
    position: absolute;
    left: 330px;
    width: 540px;
    height: 310px;
    background: var(--card);
    overflow: hidden;
    box-shadow: 0 6px 18px rgba(0,0,0,0.18);
  }
  .card--front { top: 150px; }
  .card--back { top: 540px; }

  /* Front */
  .offer-tab {
    position: absolute;
    top: 0; right: 0;
    width: 150px; height: 84px;
    background: linear-gradient(135deg, var(--blue-light), var(--blue));
    color: #fff;
    font-size: 52px;
    display: flex; align-items: center; justify-content: center;
    letter-spacing: 1px;
  }
  .brand {
    position: absolute;
    left: 44px; top: 70px;
    display: flex; align-items: center; gap: 16px;
  }
  .brand__mark {
    width: 58px; height: 58px;
    background: var(--grey);
  }
  .brand__name {
    font-size: 64px;
    color: var(--grey);
    line-height: 1;
  }
  .tagline {
    position: absolute;
    left: 44px; top: 150px;
    font-size: 34px;
    color: var(--grey);
  }
  .contact {
    position: absolute;
    left: 44px; top: 220px;
    list-style: none;
    font-size: 16px;
    color: var(--grey-light);
    letter-spacing: 1px;
  }
  .contact li { display: flex; align-items: center; gap: 12px; margin-bottom: 10px; }
  .contact svg { width: 20px; height: 20px; flex: none; }

  /* Back */
  .trade-band {
    position: absolute;
    left: 0; top: 0;
    width: 190px; height: 100%;
    background: linear-gradient(160deg, var(--blue-light), var(--blue-dark));
    display: grid;
    grid-template-columns: repeat(3, 40px);
    grid-auto-rows: 40px;
    gap: 12px;
    align-content: center;
    justify-content: center;
  }
  .trade-icon {
    border-radius: 8px;
    box-shadow: inset 0 -3px 0 rgba(0,0,0,0.15);
  }
  .trade-icon--purple { background: #a8479c; }
  .trade-icon--tan { background: #c9964a; }
  .trade-icon--grey { background: #9a9ea2; }
  .trade-icon--yellow { background: #e7c11e; }
  .trade-icon--red { background: #e24a4a; }
  .trade-icon--sky { background: #5fc4ee; }
  .trade-icon--green { background: #8cc63f; }
  .trade-icon--teal { background: #2bb3b1; }
  .trade-icon--white { background: #eef3f6; }
  .trade-icon--navy { background: #2e6fb5; }

  .back-content {
    position: absolute;
    left: 216px; top: 26px;
    width: 300px;
  }
  .headline {
    font-size: 25px;
    color: var(--blue-dark);
    font-weight: 700;
    letter-spacing: 0.2px;
    margin-bottom: 18px;
  }
  .label {
    font-size: 14px;
    color: var(--blue);
  }
  .write-line {
    border-bottom: 1px dotted #b8c2c8;
    height: 26px;
  }
  .divider {
    border: 0;
    border-top: 1px solid var(--blue);
    margin: 20px 0 10px;
  }
  .feedback-pill {
    margin-top: 12px;
    background: linear-gradient(180deg, var(--blue-light), var(--blue));
    border-radius: 18px;
    color: #fff;
    text-align: center;
    padding: 9px 10px;
    font-size: 13px;
    line-height: 1.45;
    letter-spacing: 0.6px;
  }
</style>
</head>
<body>

<section class="card card--front" aria-label="Card front">
  <div class="offer-tab">10%</div>
  <div class="brand">
    <span class="brand__mark"></span>
    <span class="brand__name">Norvale</span>
  </div>
  <p class="tagline">Expert Property Care</p>
  <ul class="contact">
    <li>
      <svg viewBox="0 0 20 20" aria-hidden="true"><circle cx="10" cy="10" r="9" fill="none" stroke="#1e9fd6" stroke-width="1.6"/><path d="M7 5.5l2 2-1 1.3c.6 1.3 1.6 2.3 2.9 2.9l1.3-1 2 2-1.2 1.3C10.2 14 6 9.8 5.7 6.7z" fill="#1e9fd6"/></svg>
      0800 012 3456
    </li>
    <li>
      <svg viewBox="0 0 20 20" aria-hidden="true"><circle cx="10" cy="10" r="9" fill="#1e9fd6"/><g fill="none" stroke="#fff" stroke-width="1"><circle cx="10" cy="10" r="5.5"/><ellipse cx="10" cy="10" rx="2.4" ry="5.5"/><path d="M4.5 10h11"/></g></svg>
      www.norvale-trades.co.uk
    </li>
  </ul>
</section>

<section class="card card--back" aria-label="Card back">
  <div class="trade-band" role="img" aria-label="Twelve trade service icons: building, plumbing, decorating, electrics, carpentry, heating and more">
    <span class="trade-icon trade-icon--purple"></span>
    <span class="trade-icon trade-icon--tan"></span>
    <span class="trade-icon trade-icon--grey"></span>
    <span class="trade-icon trade-icon--yellow"></span>
    <span class="trade-icon trade-icon--red"></span>
    <span class="trade-icon trade-icon--navy"></span>
    <span class="trade-icon trade-icon--grey"></span>
    <span class="trade-icon trade-icon--sky"></span>
    <span class="trade-icon trade-icon--white"></span>
    <span class="trade-icon trade-icon--green"></span>
    <span class="trade-icon trade-icon--tan"></span>
    <span class="trade-icon trade-icon--teal"></span>
  </div>
  <div class="back-content">
    <h1 class="headline">Your local all-trade experts</h1>
    <p class="label">Your Norvale tradesman:</p>
    <div class="write-line"></div>
    <div class="write-line"></div>
    <hr class="divider">
    <p class="label">What do you think about our service?</p>
    <div class="feedback-pill">
      Leave your feedback online<br>
      www.norvale-trades.co.uk/feedback
    </div>
  </div>
</section>

</body>
</html>
```